Consulting services and software brochure

We need a brochure designed that would ideally work with our logo and highlight a few of our consulting services and a couple products we offer. Our industry is real estate technology and we focus on consulting services for third party software systems. We would like the design to work well with our logo colors although we are open to changing either the blue or the orange to white in a design. The final design should clearly highlight our service options in an easy to read way while also leaving plenty of room to insert a lot of text on each service

What we like about our current design: it incorporates our colors well and has lots of room for text on each service, the two product offerings, and a couple testimonials from our clients

What we don’t like: It’s very busy and doesn’t highlight our offerings without a lot of reading. We also think it could have better layout, be much more polished and interesting visually (this was not designed by a professional).

Please provide source file compatible with Photoshop.

We are impressed with the designs so far and have made the payment guaranteed for this project. We will be starting to provide feedback early next week as we review internally.

Regarding size: We are open to a multi-page brochure or an 8 1/2 x 11, square shape, etc. After reviewing the designs we have decided the tri-folds seem to look too busy though on a standard piece of paper. Also, there's a good chance whatever designer we choose we will also hire to do another option in a different size/length so please don't worry either way too much about that.

Thanks for the great submissions so far!

Reason: Hi - we're extending the deadline a week since a few people providing input have been out this week for Passover and Good Friday. Thank you for your understanding.

Reason: Hi - we've settled on a designer and are now refining the brochure. Thank you everyone for your time and effort.

Real Estate

```html
<!DOCTYPE html>
<html lang="en">
<head>
<meta charset="utf-8">
<title>Real Estate Technology Consulting Brochure</title>
<link href="https://fonts.googleapis.com/css2?family=Open+Sans:ital,wght@0,400;0,600;0,700;1,700&display=swap" rel="stylesheet">
<style>
  :root {
    --green: #a9d59c;
    --green-accent: #6db35a;
    --orange: #f47b26;
    --paper: #efefef;
    --ink: #1f1f1f;
    --ink-soft: #4a4a4a;
    --rule: #3a3a3a;
    --white: #ffffff;
  }
  html, body { margin: 0; padding: 0; width: 1200px; height: 933px; overflow: hidden; background: var(--paper); }
  .sheet {
    position: absolute; left: 0; top: 0; width: 810px; height: 630px;
    transform: scale(1.48148); transform-origin: 0 0;
    font-family: "Open Sans", Arial, sans-serif; color: var(--ink);
    font-size: 7.6px; line-height: 11px;
  }
  .backdrop { position: absolute; left: 0; top: 0; }
  .section-title {
    position: absolute; margin: 0; font-weight: 400; font-size: 18px; line-height: 22px;
    letter-spacing: 0.2px; white-space: nowrap; padding-bottom: 5px;
    border-bottom: 0.8px solid var(--rule);
  }
  .section-title small { font-size: 10.5px; letter-spacing: 0.3px; }
  .section-title .corner { display: inline-block; width: 0; height: 0; margin-right: 8px;
    border-left: 12px solid transparent; border-bottom: 12px solid var(--rule); vertical-align: 1px; }
  .title-left { left: 38px; top: 36px; width: 347px; color: var(--white); }
  .title-right { left: 483px; top: 36px; width: 287px; color: var(--ink); }
  .copy { position: absolute; }
  .copy p { margin: 0 0 11px; }
  .copy b { font-weight: 700; }
  .muted { color: var(--ink-soft); }
  .accent { color: var(--green-accent); }
  .tick { color: var(--green-accent); font-weight: 700; }
  .callout { position: absolute; left: 427px; top: 178px; margin: 0; font-weight: 400;
    font-size: 15.5px; line-height: 20px; color: var(--white); white-space: nowrap; }
  .callout .tick-mark { font-weight: 700; margin-right: 5px; }
  .quote { font-weight: 700; font-style: italic; }
  .brand { position: absolute; left: 598px; top: 548px; display: flex; align-items: center; gap: 6px; }
  .brand-square { width: 14px; height: 14px; background: var(--orange); }
  .brand-name { font-size: 15px; font-weight: 700; color: var(--ink); white-space: nowrap; }
</style>
</head>
<body>
<div class="sheet">
  <svg class="backdrop" width="810" height="630" viewBox="0 0 810 630">
    <defs>
      <linearGradient id="g-laptop" x1="0" y1="0" x2="1" y2="1">
        <stop offset="0" stop-color="#dfe6ee"/><stop offset="0.5" stop-color="#7d8da0"/><stop offset="1" stop-color="#2e3846"/>
      </linearGradient>
      <linearGradient id="g-stylus" x1="0" y1="0" x2="1" y2="1">
        <stop offset="0" stop-color="#fafafa"/><stop offset="0.6" stop-color="#d9d3cd"/><stop offset="1" stop-color="#5a5a5c"/>
      </linearGradient>
      <linearGradient id="g-meeting" x1="0" y1="0" x2="1" y2="1">
        <stop offset="0" stop-color="#c7d3dd"/><stop offset="0.5" stop-color="#5d6670"/><stop offset="1" stop-color="#1e2226"/>
      </linearGradient>
      <linearGradient id="g-caller" x1="0" y1="0" x2="1" y2="1">
        <stop offset="0" stop-color="#f2f2f2"/><stop offset="0.6" stop-color="#c8b8a8"/><stop offset="1" stop-color="#4a4e55"/>
      </linearGradient>
    </defs>
    <rect width="810" height="630" fill="var(--paper)"/>
    <polygon fill="var(--green)" points="0,0 405,0 600,195 390,405 285,300 180,405 0,225"/>
    <polygon fill="var(--green)" points="390,405 495,300 600,405 705,300 810,195 810,630 405,630 285,510"/>
    <polygon fill="var(--orange)" points="285,300 390,405 285,510 180,405"/>
    <polygon fill="var(--orange)" points="495,90 600,195 495,300 390,195"/>
    <polygon role="img" aria-label="Photo: hand typing on a laptop keyboard, businessman in suit and blue tie" fill="url(#g-laptop)" points="180,195 285,300 180,405 75,300"/>
    <polygon role="img" aria-label="Photo: hands using a stylus on a handheld device" fill="url(#g-stylus)" points="390,195 495,300 390,405 285,300"/>
    <polygon role="img" aria-label="Photo: business team meeting around a laptop in an office" fill="url(#g-meeting)" points="600,195 705,300 600,405 495,300"/>
    <polygon role="img" aria-label="Photo: businessman talking on a mobile phone" fill="url(#g-caller)" points="810,195 915,300 810,405 705,300"/>
  </svg>

  <h2 class="section-title title-left"><span class="corner"></span>LOREM IPSUM <small>DOLOR SIT AMET</small></h2>
  <h2 class="section-title title-right"><span class="corner"></span>DUIS AUTE IRURE <small>EX EA COMMODO</small></h2>

  <div class="copy" style="left:38px; top:75px; width:212px;">
    <p><b>Lorem ipsum dolor sit amet,</b> consectetur adipisicing elit, sed do eiusmod tempor incididunt ut labore et dolore magna aliqua.</p>
    <p>Ut enim ad minim veniam, quis nostrud exercitation ullamco laboris nisi ut aliquip ex ea commodo consequat. Duis aute irure dolor in reprehenderit in voluptate id est laborum.</p>
  </div>

  <div class="copy" style="left:270px; top:78px; width:120px;">
    <p>Lorem ipsum dolor sit amet, sed do eiusmod incididunt ut labore et dolore aliqua.</p>
    <p><b><span class="tick">✔</span> Ut enim ad minim veniam, quis nostrud exercitation ullamco laboris nisi ut aliquip.</b></p>
  </div>

  <div class="copy" style="left:566px; top:78px; width:206px;">
    <p><b>Lorem ipsum dolor sit amet,</b> consectetur adipisicing elit, sed do eiusmod tempor incididunt ut labore et dolore magna aliqua.</p>
    <p class="muted">Ut enim ad minim veniam, quis nostrud exercitation ullamco laboris nisi ut aliquip <span class="accent">ex ea commodo consequat.</span></p>
  </div>
  <div class="copy" style="left:598px; top:166px; width:176px; text-align:center;">
    <p><b>Duis aute irure dolor in reprehenderit in voluptate velit esse cillum dolore eu fugiat nulla pariatur.</b></p>
  </div>

  <p class="callout"><span class="tick-mark">✔</span>UT ENIM AD MINIM</p>

  <div class="copy" style="left:38px; top:385px; width:210px;">
    <p>Lorem ipsum dolor sit<br>amet, consectetur adipisi-<br>cing elit, sed do eiusmod<br>tempor incididunt ut labore et<br>dolore magna aliqua.</p>
    <p><b>Ut enim ad minim veniam, quis nostrud exercitation ullamco laboris nisi ut aliquip</b> ex ea commodo consequat.</p>
    <p>Duis aute irure dolor in reprehenderit in voluptate velit esse cillum dolore eu fugiat nulla pariatur.</p>
    <p>Excepteur sint occaecat cupidatat non proident, sunt in culpa qui officia deserunt mollit anim id est laborum.</p>
  </div>

  <div class="copy" style="left:425px; top:422px; width:135px;">
    <p>Lorem ipsum dolor sit amet, consectetur adipisicing elit, sed do eiusmod tempor incididunt ut labore et dolore magna aliqu</p>
    <p>a. <b>Ut enim ad minim veniam, quis nostrud exercitation</b> ullamco laboris nisi ut aliquip ex ea commodo consequat.<br>Lorem ipsum dolor sit amet,</p>
  </div>

  <div class="copy" style="left:573px; top:422px; width:190px;">
    <p>consectetur adipisicing elit, sed do eiusmod tempor incididunt ut labore et dolore magna aliqua.</p>
    <p class="quote">Ut enim ad minim veniam, quis nostrud exerci-tation ullamco laboris nisi ut aliquip ex ea commodo consequat.</p>
  </div>

  <div class="brand">
    <span class="brand-square"></span>
    <span class="brand-name">Northgate Realty Tech</span>
  </div>
</div>
</body>
</html>
```